Massage-Creme label for a young pharmacy

We are a young pharmacy which is part of a big union. We developed for a customer a very good massage creme with aloe vera, coconut oil, and many more advantages and as well a massage jelly. All we need is a good and affordable label which is beatiful and helps us to promote our product. As we want to develop further products, it would be very cool to have a corporate label for all upcoming products.

Target Market(s)

professional masseurs and physiotherapists

Industry/Entity Type

Health And Wellness

Font styles to use
Sans Serif
Decorative

Colors

Designer to choose colors to be used in the design.

Requirements
Must have
• Professionally looking design (but I'm sure you are doing so... :-)
Nice to have
• Label can have any shape. What you see is just a bad label with corresponding sizes, so you can imagine how it would look like in the final state.
Should not have
• If possible, the label should not be completely black (although it might look cool) as we are printing it on our own Varnick tq318-dm and black is difficult to print (and very costy).

```html
<!DOCTYPE html>
<html lang="de">
<head>
<meta charset="utf-8">
<title>Massage Crème – Etiketten</title>
<link href="https://fonts.googleapis.com/css2?family=Montserrat:wght@300;400;500&display=swap" rel="stylesheet">
<style>
  :root {
    --page: #f5f5f5;
    --label: #ffffff;
    --ink: #2b2b2b;
    --muted: #555555;
    --soft: #d9d9d9;
    --ornament-light: #e4e4e4;
    --ornament-dark: #9a9a9a;
    --accent: #d3242d;
    --band: #1c1c1c;
  }
  * { box-sizing: border-box; margin: 0; padding: 0; }
  html, body { width: 1200px; height: 1200px; overflow: hidden; }
  body {
    background: var(--page);
    font-family: "Montserrat", sans-serif;
    color: var(--ink);
    position: relative;
  }
  .label {
    position: absolute;
    top: 240px;
    width: 300px;
    height: 680px;
    background: var(--label);
    box-shadow: 0 6px 24px rgba(0,0,0,0.08);
    overflow: hidden;
  }
  .label--front { left: 230px; }
  .label--back { left: 670px; }
  .label__band {
    position: absolute; left: 0; right: 0; bottom: 0; height: 40px;
    background: var(--band);
  }

  /* Front */
  .mandala {
    position: absolute; left: 20px; top: 40px; width: 260px; height: 260px;
    border-radius: 50%;
    background: radial-gradient(circle, var(--accent) 0 5%, #ffffff 6% 14%, var(--band) 15% 42%, var(--ornament-light) 43% 100%);
  }
  .front__title {
    position: absolute; top: 340px; left: 0; right: 0; text-align: center;
    font-weight: 400; font-size: 26px; letter-spacing: 0.5px;
  }
  .front__title .accent { color: var(--accent); }
  .front__sub {
    position: absolute; top: 378px; left: 0; right: 0; text-align: center;
    font-size: 11px; font-weight: 400; color: var(--muted); letter-spacing: 0.3px;
  }
  .front__dots {
    position: absolute; top: 405px; left: 148px;
    display: flex; flex-direction: column; gap: 22px;
  }
  .front__dots span { width: 4px; height: 4px; border-radius: 50%; background: var(--ink); display: block; }
  .front__volume {
    position: absolute; bottom: 56px; left: 0; right: 0; text-align: center;
    font-size: 15px; font-weight: 300;
  }

  /* Back */
  .back__ornament {
    position: absolute; right: -60px; top: 360px; width: 300px; height: 260px;
    border-radius: 50%;
    background: radial-gradient(circle, #ececec 0%, var(--ornament-light) 50%, rgba(228,228,228,0) 72%);
  }
  .back__content { position: absolute; inset: 0; padding: 36px 16px 0; text-align: center; }
  .back__title { font-size: 15px; font-weight: 400; }
  .back__title .accent { color: var(--accent); }
  .back__sub { font-size: 6px; font-weight: 500; margin-top: 2px; }
  .back__copy { font-size: 9px; line-height: 1.55; color: var(--muted); margin-top: 24px; }
  .back__copy p + p { margin-top: 12px; }
  .ph-scale {
    margin: 6px auto 0; width: 210px; height: 8px; position: relative;
  }
  .ph-scale::before {
    content: ""; position: absolute; left: 0; right: 0; top: 4px; height: 1px; background: var(--ink);
  }
  .ph-scale::after {
    content: ""; position: absolute; left: 80px; top: 1px; width: 5px; height: 5px;
    border: 1px solid var(--ink); border-radius: 50%; background: var(--label);
  }
  .back__ingredients {
    font-size: 7px; line-height: 1.55; color: var(--muted); text-align: justify;
    margin-top: 34px; position: relative;
  }
  .back__note { font-size: 7px; line-height: 1.5; color: var(--muted); margin-top: 12px; position: relative; }
  .back__box {
    border: 1px solid var(--muted); padding: 4px 8px; margin-top: 10px;
    font-size: 7px; line-height: 1.5; color: var(--muted); position: relative;
  }
  .brand {
    position: absolute; right: 52px; bottom: 118px;
    display: flex; align-items: center; gap: 5px;
    font-size: 10px; font-weight: 500; color: var(--ink);
  }
  .brand__mark { width: 7px; height: 7px; background: var(--accent); }
  .back__lot {
    position: absolute; left: 16px; bottom: 60px;
    font-size: 7.5px; line-height: 1.4; color: var(--ink); text-align: left;
  }
  .back__lot b { font-weight: 500; display: inline-block; width: 22px; }
  .back__address {
    position: absolute; right: 16px; bottom: 60px;
    font-size: 6px; line-height: 1.5; color: var(--muted); text-align: left;
  }
</style>
</head>
<body>

  <section class="label label--front">
    <div class="mandala" role="img" aria-label="Rundes Mandala-Ornament in Schwarz und Hellgrau mit rotem Stern in der Mitte"></div>
    <h1 class="front__title">MASSAGE CR<span class="accent">È</span>ME</h1>
    <p class="front__sub">ALOE VERA &amp; COCONUT OIL</p>
    <div class="front__dots"><span></span><span></span><span></span><span></span><span></span></div>
    <p class="front__volume">1000 ml</p>
    <div class="label__band"></div>
  </section>

  <section class="label label--back">
    <div class="back__ornament" role="img" aria-label="Hellgraues Ornament als Hintergrunddekor"></div>
    <div class="back__content">
      <h2 class="back__title">MASSAGE CR<span class="accent">È</span>ME</h2>
      <p class="back__sub">ALOE VERA &amp; COCONUT OIL</p>
      <div class="back__copy">
        <p>Hochwertige und sehr hautschonende Emulsion mit hervorragendem Gleitverhalten für die professionelle Massage.</p>
        <p>Hilft durch den hohen Gehalt an Aloe Vera Gel (50%), die Feuchtigkeit der Haut zu erhalten und schützt durch die Zugabe von Panthenol (=Provitamin B5) und Allantoin vor Hautreizungen.</p>
        <p>Speziell für die (bio-)energetische Massage entwickelt.</p>
        <p>pH-neutral für die Haut (pH-Wert = 5.5)</p>
      </div>
      <div class="ph-scale"></div>
      <p class="back__ingredients">Zus : water (aqua), cetearyl isononanoate, ethylhexyl stearate, cocos nucifera (coconut oil), octyldodecanol, glycerol, glyceryl stearate citrate, cetearyl alcohol, phenoxyethanol (and) caprylyl glycol, panthenol, sodium chloride, xanthan gum, disodium hydrogenphosphate, citric acid, aloe barbadensis leaf juice extract, allantoin, parfum.</p>
      <p class="back__note">Bei der Entwicklung unserer Produkte legen wir grössten Wert auf gute Verträglichkeit und hochwertige Rohstoffe.</p>
      <p class="back__box">Dieses Produkt ist frei von Parabenen, Mineralölen (Paraffin/Vaseline), Silikonen, Farbstoffen und Mikroplastik (Acrylate).</p>
    </div>
    <div class="brand"><span class="brand__mark"></span>Brisant · Apotheke Dr. Lenwald</div>
    <p class="back__lot"><b>Exp</b>: 03.2021<br><b>Lot</b>: 913015/A</p>
    <p class="back__address">Lindenweg 12, 8000 Musterdorf<br>Tel. 044 000 12 34, Fax 044 000 12 35<br>www.apotheke-lenwald.ch</p>
    <div class="label__band"></div>
  </section>

</body>
</html>
```